Personal Finance e-commerce website needs a simple budget design

Hello! I am starting to sell downloadable and printable budget planners, as shown in the attached file, for people to plan ahead on their personal finances. <br/><br/>I want to see a one-page design with similar columns (for example, "Expenses, Budget, and Actual"). I would also like to see the basic formula ("Net Income = Gross income - Total Expenses") somewhere on the design. Finally, I want the design to remain mostly minimalistic and simple for the average person to plan their personal monthly budgets.<br/><br/>However, other than that, the overall design, layout, and colors will be at the graphic designer's choice. If you have any questions for me, please let me know. Thank you for your time!

Industry/Entity Type

Financial Planning

Colors

Designer to choose colors to be used in the design.

Requirements
Must have
• I want to see a one-page design with similar columns (for example, "Expenses, Budget, and Actual").
• I want the design to remain mostly minimalistic and simple for the average person to plan their personal monthly budgets.
Nice to have
• I would also like to see the basic formula ("Net Income = Gross income - Total Expenses") somewhere on the design.

```html
<!DOCTYPE html>
<html lang="en">
<head>
<meta charset="UTF-8">
<title>Monthly Budget Planner</title>
<link rel="stylesheet" href="https://fonts.googleapis.com/css2?family=Bebas+Neue&family=Barlow:wght@500;600&display=swap">
<style>
  :root {
    --yellow: #fecb0a;
    --black: #000000;
    --white: #ffffff;
    --row-dark: #d5d6d8;
    --row-light: #f1f1f2;
  }
  * { margin: 0; padding: 0; box-sizing: border-box; }
  html, body { width: 848px; height: 1200px; overflow: hidden; background: var(--white); }
  .sheet { position: relative; width: 848px; height: 1200px; background: var(--white); overflow: hidden; }

  .accent-bar { position: absolute; top: 60px; height: 61px; background: var(--yellow); }
  .accent-bar--left { left: 0; width: 340px; }
  .accent-bar--right { left: 752px; width: 96px; }
  .sheet-title {
    position: absolute; left: 354px; top: 61px;
    font-family: "Bebas Neue", "Oswald", sans-serif; font-weight: 400;
    font-size: 74px; line-height: 70px; color: var(--black);
    letter-spacing: 0; white-space: nowrap;
    transform: scaleX(0.92); transform-origin: left top;
  }

  .budget-table { position: absolute; left: 48px; top: 158px; width: 749px; }
  .budget-row { display: flex; gap: 5px; }
  .budget-cell { flex: none; }
  .col-expenses { width: 338px; }
  .col-budget { width: 200px; }
  .col-actual { width: 201px; }
  .budget-row--head .budget-cell {
    height: 49px; background: var(--black); color: var(--white);
    font-family: "Barlow", sans-serif; font-weight: 500; font-size: 25px;
    display: flex; align-items: center; justify-content: center; white-space: nowrap;
  }
  .budget-row--entry:nth-child(even) .budget-cell { height: 70px; background: var(--row-dark); }
  .budget-row--entry:nth-child(odd) .budget-cell { height: 60.5px; background: var(--row-light); }

  .formula-band { position: absolute; left: 0; top: 1083px; width: 848px; height: 68px; background: var(--yellow); }
  .formula-term {
    position: absolute; top: 0; height: 68px; line-height: 68px;
    font-family: "Barlow", sans-serif; font-weight: 600; font-size: 30px;
    color: var(--black); white-space: nowrap;
  }
  .formula-term--net { left: 69px; }
  .formula-term--equals { left: 262px; }
  .formula-term--gross { left: 295px; }
  .formula-term--minus { left: 515px; }
  .formula-term--total { left: 544px; }
  .footer-band { position: absolute; left: 0; top: 1151px; width: 848px; height: 49px; background: var(--black); }
</style>
</head>
<body>
<div class="sheet">
  <div class="accent-bar accent-bar--left"></div>
  <h1 class="sheet-title">MONTHLY BUDGET</h1>
  <div class="accent-bar accent-bar--right"></div>

  <div class="budget-table" role="table" aria-label="Monthly budget">
    <div class="budget-row budget-row--head" role="row">
      <div class="budget-cell col-expenses" role="columnheader">EXPENSES</div>
      <div class="budget-cell col-budget" role="columnheader">BUDGET (USD)</div>
      <div class="budget-cell col-actual" role="columnheader">ACTUAL (USD)</div>
    </div>
    <div class="budget-row budget-row--entry" role="row"><div class="budget-cell col-expenses"></div><div class="budget-cell col-budget"></div><div class="budget-cell col-actual"></div></div>
    <div class="budget-row budget-row--entry" role="row"><div class="budget-cell col-expenses"></div><div class="budget-cell col-budget"></div><div class="budget-cell col-actual"></div></div>
    <div class="budget-row budget-row--entry" role="row"><div class="budget-cell col-expenses"></div><div class="budget-cell col-budget"></div><div class="budget-cell col-actual"></div></div>
    <div class="budget-row budget-row--entry" role="row"><div class="budget-cell col-expenses"></div><div class="budget-cell col-budget"></div><div class="budget-cell col-actual"></div></div>
    <div class="budget-row budget-row--entry" role="row"><div class="budget-cell col-expenses"></div><div class="budget-cell col-budget"></div><div class="budget-cell col-actual"></div></div>
    <div class="budget-row budget-row--entry" role="row"><div class="budget-cell col-expenses"></div><div class="budget-cell col-budget"></div><div class="budget-cell col-actual"></div></div>
    <div class="budget-row budget-row--entry" role="row"><div class="budget-cell col-expenses"></div><div class="budget-cell col-budget"></div><div class="budget-cell col-actual"></div></div>
    <div class="budget-row budget-row--entry" role="row"><div class="budget-cell col-expenses"></div><div class="budget-cell col-budget"></div><div class="budget-cell col-actual"></div></div>
    <div class="budget-row budget-row--entry" role="row"><div class="budget-cell col-expenses"></div><div class="budget-cell col-budget"></div><div class="budget-cell col-actual"></div></div>
    <div class="budget-row budget-row--entry" role="row"><div class="budget-cell col-expenses"></div><div class="budget-cell col-budget"></div><div class="budget-cell col-actual"></div></div>
    <div class="budget-row budget-row--entry" role="row"><div class="budget-cell col-expenses"></div><div class="budget-cell col-budget"></div><div class="budget-cell col-actual"></div></div>
    <div class="budget-row budget-row--entry" role="row"><div class="budget-cell col-expenses"></div><div class="budget-cell col-budget"></div><div class="budget-cell col-actual"></div></div>
    <div class="budget-row budget-row--entry" role="row"><div class="budget-cell col-expenses"></div><div class="budget-cell col-budget"></div><div class="budget-cell col-actual"></div></div>
  </div>

  <div class="formula-band">
    <span class="formula-term formula-term--net">NET INCOME</span>
    <span class="formula-term formula-term--equals">=</span>
    <span class="formula-term formula-term--gross">GROSS INCOME</span>
    <span class="formula-term formula-term--minus">-</span>
    <span class="formula-term formula-term--total">TOTAL EXPENSES</span>
  </div>
  <div class="footer-band"></div>
</div>
</body>
</html>
```